Lavoie Roofing

Want a professional looking business card

Industry/Entity Type

Business

Contact Information for Business Card

Mark Lavoie ( Owner) mark@lavoieroofing.example, www.lavoieroofing.example, Adress: 4712 County road 31 Brookvale,NS B0K2M4

```html
<!DOCTYPE html>
<html lang="en">
<head>
<meta charset="utf-8">
<title>Lavoie Roofing – Business Card</title>
<link href="https://fonts.googleapis.com/css2?family=Roboto+Condensed:wght@400;700&family=Roboto:wght@400;500&display=swap" rel="stylesheet">
<style>
  :root {
    --stage: #5d6469;
    --stage-edge: #3f4448;
    --brand-blue: #1e4785;
    --paper: #ffffff;
    --ink: #222222;
    --logo-grey: #8a8c8f;
  }
  * { box-sizing: border-box; margin: 0; padding: 0; }
  html, body { width: 1200px; height: 900px; overflow: hidden; }
  body {
    background: radial-gradient(ellipse at 50% 45%, var(--stage) 0%, var(--stage-edge) 100%);
    display: flex; flex-direction: column; align-items: center; justify-content: center;
    gap: 44px;
    font-family: "Roboto", Arial, sans-serif;
  }
  .card {
    width: 620px; height: 354px; position: relative;
    box-shadow: 0 14px 30px rgba(0,0,0,.35);
  }
  .card--front { background: var(--paper); }
  .wordmark {
    font-family: "Roboto Condensed", Arial, sans-serif;
    font-weight: 700; text-transform: uppercase; letter-spacing: 3px;
    display: flex; align-items: center; gap: 10px; white-space: nowrap;
  }
  .wordmark__square { width: 14px; height: 14px; flex: none; }
  .card--front .wordmark {
    position: absolute; top: 46px; left: 258px;
    color: var(--brand-blue); font-size: 32px;
  }
  .card--front .wordmark__square { background: var(--brand-blue); }
  .holder {
    position: absolute; left: 56px; top: 150px;
    font-family: "Roboto Condensed", Arial, sans-serif;
  }
  .holder__name { color: var(--brand-blue); font-size: 28px; font-weight: 700; }
  .holder__role { color: var(--ink); font-size: 15px; margin-top: 2px; }
  .divider {
    position: absolute; left: 262px; top: 140px; width: 2px; height: 150px;
    background: linear-gradient(to bottom, rgba(30,71,133,0), var(--brand-blue) 50%, rgba(30,71,133,0));
    transform: rotate(20deg);
  }
  .contact {
    position: absolute; left: 320px; top: 150px;
    font-size: 15px; color: var(--ink); line-height: 1.5;
    list-style: none; white-space: nowrap;
  }
  .contact__address { margin-bottom: 8px; }
  .contact__item { display: flex; align-items: center; gap: 10px; }
  .contact__icon { width: 14px; height: 14px; flex: none; fill: var(--brand-blue); }
  .card--back {
    background: var(--brand-blue);
    display: flex; flex-direction: column; align-items: center; justify-content: center; gap: 40px;
  }
  .card--back .wordmark { color: var(--paper); font-size: 46px; }
  .card--back .wordmark__square { background: var(--paper); width: 18px; height: 18px; }
  .card--back .website { color: var(--paper); font-size: 15px; letter-spacing: .5px; }
</style>
</head>
<body>

<section class="card card--front" aria-label="Business card front">
  <div class="wordmark"><span class="wordmark__square"></span>Lavoie Roofing</div>

  <div class="holder">
    <p class="holder__name">Mark Lavoie</p>
    <p class="holder__role">Owner</p>
  </div>

  <div class="divider"></div>

  <ul class="contact">
    <li class="contact__address">4712 County road 31<br>Brookvale,NS B0K2M4</li>
    <li class="contact__item">
      <svg class="contact__icon" viewBox="0 0 24 24"><path d="M6.6 10.8a15 15 0 0 0 6.6 6.6l2.2-2.2a1 1 0 0 1 1-.25 11.4 11.4 0 0 0 3.6.57 1 1 0 0 1 1 1V20a1 1 0 0 1-1 1A17 17 0 0 1 3 4a1 1 0 0 1 1-1h3.5a1 1 0 0 1 1 1c0 1.25.2 2.45.57 3.57a1 1 0 0 1-.25 1z"/></svg>
      (555) 010-0142
    </li>
    <li class="contact__item">
      <svg class="contact__icon" viewBox="0 0 24 24"><path d="M2 5h20v14H2z M2 5l10 8 10-8" stroke="#fff" stroke-width="1.5"/></svg>
      mark@lavoieroofing.example
    </li>
    <li class="contact__item">
      <svg class="contact__icon" viewBox="0 0 24 24"><circle cx="12" cy="12" r="10"/><path d="M2 12h20M12 2c3 3 3 17 0 20M12 2c-3 3-3 17 0 20" stroke="#fff" stroke-width="1.4" fill="none"/></svg>
      www.lavoieroofing.example
    </li>
  </ul>
</section>

<section class="card card--back" aria-label="Business card back">
  <div class="wordmark"><span class="wordmark__square"></span>Lavoie Roofing</div>
  <p class="website">www.lavoieroofing.example</p>
</section>

</body>
</html>
```